Update Old OR create new Website

Current Website is looking a bit old, I did this one a few years back.

Would like a fresh new look, current website sitepress theme is " the Vanta theme" from plumcrate and I just purchased this theme - "bravlo" also from plumcrate, I quite like the look of - http://bravlo.quorvex-skins.com/tech-business/ and if we could get somthing simlar would be great.

current website is at http://www.hle.com.au, have been playing around with the slider that i like.

I have said 5 pages to be designed but really it is just a 5 page website where most pages will look the same.

Any questions please let me know

Target Market(s)

Business

Coding

Coded - Design and coding required

Number of Pages Required

5+ page

Font styles to use
Sans Serif

Colors
33a6d7
0292cd
ffffff
0255a3

Requirements
Must have
• Device compatibility - pc, tablet, phone
Nice to have
• video
Should not have
• vunerabilities. Must also use images that will expire or disappear, ie must be uploaded to site not links to elsewhere.

```html
<!DOCTYPE html>
<html lang="en">
<head>
<meta charset="utf-8">
<title>HLE Technologies</title>
<link href="https://fonts.googleapis.com/css2?family=Roboto:wght@400;500;700;900&family=Open+Sans:ital,wght@0,400;0,600;0,700;1,400&display=swap" rel="stylesheet">
<style>
:root{
  --blue:#0292cd;
  --blue-light:#33a6d7;
  --blue-deep:#0255a3;
  --ink:#1e1e1e;
  --text:#555;
  --muted:#888;
  --line:#d9d9d9;
  --white:#fff;
  --dark:#24303a;
}
*{box-sizing:border-box;margin:0;padding:0}
html,body{width:1200px;height:2922px;overflow:hidden;background:var(--white)}
body{font-family:"Open Sans",Arial,sans-serif;color:var(--text)}
.page{position:relative;width:1200px;height:2922px;overflow:hidden}
.abs{position:absolute}
svg{display:block}

/* header */
.header{left:0;top:0;width:1200px;height:101px;border-top:5px solid var(--blue-deep);background:var(--white)}
.brand{left:97px;top:22px;display:flex;align-items:center;gap:10px}
.brand-dot{width:44px;height:44px;border-radius:50%;background:var(--blue)}
.brand-name{font-family:"Roboto",sans-serif;font-weight:700;font-size:24px;color:var(--ink)}
.contact-bar{right:97px;top:18px;display:flex;gap:30px;font-family:"Roboto",sans-serif;font-size:16px;color:var(--ink)}
.contact-bar span{display:flex;align-items:center;gap:10px}
.ring{width:30px;height:30px;border:1.5px solid var(--blue);border-radius:50%;display:flex;align-items:center;justify-content:center}
.nav{right:97px;top:64px;display:flex;gap:24px;font-family:"Roboto",sans-serif;font-weight:700;font-size:15.5px;color:var(--ink);align-items:center}
.nav .active{color:var(--blue)}

/* hero */
.hero{left:0;top:101px;width:1200px;height:487px;background:linear-gradient(180deg,#5a6478 0%,#7b7080 40%,#b8804a 70%,#3c3c44 100%)}
.hero-title{left:0;top:200px;width:1200px;text-align:center;font-family:"Roboto",sans-serif;font-weight:700;font-size:64px;color:var(--white);letter-spacing:1px}
.hero-sub{left:0;top:285px;width:1200px;text-align:center;font-size:24px;line-height:37px;color:var(--white)}
.btn-ghost{left:508px;top:386px;width:186px;height:47px;border:2px solid var(--white);border-radius:24px;color:var(--white);font-family:"Roboto",sans-serif;font-weight:500;font-size:15px;display:flex;align-items:center;justify-content:center}
.dots{left:566px;top:519px;display:flex;gap:6px}
.dots i{width:13px;height:13px;border:2px solid var(--white);border-radius:50%}
.dots i.on{background:var(--white)}
.tab{left:561px;top:550px;width:78px;height:78px;border-radius:50%;background:var(--white);display:flex;align-items:flex-start;justify-content:center;padding-top:18px}
.tab i{width:26px;height:26px;border-radius:4px;background:var(--blue)}

/* welcome */
.welcome-title{left:97px;top:682px;font-family:"Roboto",sans-serif;font-weight:700;font-size:29px;color:var(--ink)}
.welcome-copy{left:97px;top:737px;width:460px;font-size:13.5px;line-height:24px;color:var(--text)}
.welcome-copy p+p{margin-top:24px}
.btn-line{height:40px;border:1.5px solid #bbb;border-radius:20px;font-family:"Roboto",sans-serif;font-weight:700;font-size:13px;color:var(--blue);display:flex;align-items:center;justify-content:center}
.video{left:600px;top:678px;width:503px;height:329px;border:1px solid var(--line);padding:5px;background:var(--white)}
.video-fill{width:100%;height:100%;background:linear-gradient(135deg,#cfd8e2,#eef1f4 50%,#9aa8ba);position:relative}
.play{position:absolute;left:220px;top:128px;width:58px;height:58px;border-radius:50%;background:#111;display:flex;align-items:center;justify-content:center}

/* services */
.services{left:0;top:1095px;width:1200px;height:444px;background:linear-gradient(135deg,#1b5fa8,var(--blue) 60%,#1a6bb4)}
.section-title{left:0;width:1200px;text-align:center;font-family:"Roboto",sans-serif;font-weight:700;font-size:27px}
.service{width:330px;display:flex;gap:22px}
.service-icon{flex:none;width:78px;height:78px;border:2px solid rgba(255,255,255,.85);border-radius:50%;display:flex;align-items:center;justify-content:center}
.service h3{font-family:"Roboto",sans-serif;font-weight:500;font-size:20px;color:var(--white);margin:4px 0 8px}
.service p{font-size:13px;line-height:24px;color:#e2eef8}

/* blog */
.post{width:316px}
.post-img{width:316px;height:222px;border:1px solid var(--line);padding:5px}
.post-img div{width:100%;height:100%}
.post h3{font-family:"Roboto",sans-serif;font-weight:500;font-size:20px;color:var(--ink);margin-top:28px}
.meta{display:flex;align-items:center;gap:8px;font-size:13px;color:var(--text);margin-top:12px}
.meta .sep{margin:0 4px}
.post p{font-size:13px;line-height:22px;color:var(--text);margin-top:12px}
.post .btn-line{width:110px;height:38px;margin-top:26px;font-size:12px}

/* reviews */
.reviews{left:0;top:2207px;width:1200px;height:357px;background:linear-gradient(90deg,#2a3540,#3b4852 50%,#2b363f)}
.review{width:320px;display:flex;gap:18px}
.avatar{flex:none;width:74px;height:74px;border-radius:50%;border:3px solid var(--white);background:linear-gradient(135deg,#c9c2bb,#8d8680)}
.review .quote{font-size:12px;font-style:italic;line-height:24px;color:var(--white)}
.review .quote b{font-size:20px;font-style:normal;margin-right:6px}
.review .who{font-family:"Roboto",sans-serif;font-weight:700;font-size:10.5px;color:var(--white);margin-top:14px;text-transform:uppercase}
.review .role{font-size:10px;font-style:italic;color:#dfe5ea;margin-top:4px}
.arrow{width:36px;height:36px;border:1.5px solid rgba(255,255,255,.8);border-radius:50%;display:flex;align-items:center;justify-content:center}

/* footer */
.footer h4{font-family:"Roboto",sans-serif;font-weight:700;font-size:16px;color:var(--ink)}
.links{list-style:none;font-size:12.5px;line-height:19.7px;color:var(--text);margin-top:20px}
.footer p{font-size:12.5px;line-height:21px;color:var(--text)}
.field{width:255px;border-bottom:1px solid var(--line);font-size:12px;color:#aaa;padding:10px 16px}
.contact-row{display:flex;gap:18px;font-size:12.5px;line-height:21px;color:var(--text)}
.rule{left:97px;top:2850px;width:1006px;height:1px;background:var(--line)}
.copy{left:97px;top:2880px;font-size:12px;color:var(--text)}
.social{left:976px;top:2872px;display:flex;gap:11px}
.social i{width:25px;height:25px;border:1.5px solid var(--blue);border-radius:50%}
</style>
</head>
<body>
<div class="page">

  <header class="header abs">
    <div class="brand abs" style="left:0;top:17px;position:relative"></div>
  </header>
  <div class="brand abs"><span class="brand-dot"></span><span class="brand-name">HLE Technologies</span></div>
  <div class="contact-bar abs">
    <span><i class="ring"><svg width="14" height="14" viewBox="0 0 24 24"><path fill="#0292cd" d="M6.6 10.8a15 15 0 006.6 6.6l2.2-2.2c.3-.3.7-.4 1-.2 1.1.4 2.3.6 3.6.6.6 0 1 .4 1 1V20c0 .6-.4 1-1 1A17 17 0 013 4c0-.6.4-1 1-1h3.5c.6 0 1 .4 1 1 0 1.3.2 2.5.6 3.6.1.3 0 .7-.2 1z"/></svg></i>1300 555 014</span>
    <span><i class="ring"><svg width="14" height="14" viewBox="0 0 24 24"><path fill="#0292cd" d="M2 5h20v14H2zm2 2v.5l8 5 8-5V7l-8 5z"/></svg></i>info@hle.com.au</span>
  </div>
  <nav class="nav abs">
    <span class="active">HOME</span><span>SERVERS</span><span>NETWORKS</span><span>MANAGED IT</span><span>WEB</span><span>APP'S</span><span>INTERNET</span><span>CONTACT</span>
    <svg width="16" height="16" viewBox="0 0 24 24"><circle cx="10" cy="10" r="6.5" fill="none" stroke="#1e1e1e" stroke-width="3"/><path d="M15 15l6 6" stroke="#1e1e1e" stroke-width="3"/></svg>
  </nav>

  <section class="hero abs" role="img" aria-label="City skyline with towers at sunset"></section>
  <h1 class="hero-title abs">HLE TECHNOLOGIES</h1>
  <p class="hero-sub abs">With a decade of experience, HLE Technologies understands<br>the challenges faced by SMEs</p>
  <div class="btn-ghost abs">GET MORE INFO</div>
  <div class="dots abs"><i class="on"></i><i></i><i></i><i></i></div>
  <div class="tab abs"><i></i></div>

  <h2 class="welcome-title abs">WELCOME TO HLE TECHNOLOGIES</h2>
  <div class="welcome-copy abs">
    <p>With a decade of experience, HLE Technologies understands the challenges faced by SMEs.</p>
    <p>So when we design and build networks, support solutions, hardware and software there's room for growth, change and mobility. HLE Technologies staff are not just short-term problem solvers – they are advanced systems designers and proactive thinkers who work closely with clients on issue detection and prevention.</p>
  </div>
  <div class="btn-line abs" style="left:97px;top:958px;width:125px">READ MORE</div>
  <div class="video abs">
    <div class="video-fill" role="img" aria-label="Business team reviewing charts on paper and a laptop">
      <div class="play"><svg width="20" height="22" viewBox="0 0 20 22"><path d="M3 2l15 9-15 9z" fill="#fff"/></svg></div>
    </div>
  </div>

  <section class="services abs" role="img" aria-label="Blue-tinted office workspace background"></section>
  <h2 class="section-title abs" style="top:1172px;color:var(--white)">WHAT WE DO</h2>

  <div class="service abs" style="left:97px;top:1243px">
    <div class="service-icon"><svg width="34" height="34" viewBox="0 0 24 24"><path fill="#fff" d="M12 8a4 4 0 100 8 4 4 0 000-8zm9 5.4v-2.8l-2.4-.5a7 7 0 00-.7-1.6l1.4-2-2-2-2 1.4a7 7 0 00-1.6-.7L13.4 3h-2.8l-.5 2.4a7 7 0 00-1.6.7l-2-1.4-2 2 1.4 2a7 7 0 00-.7 1.6L3 10.6v2.8l2.4.5c.2.6.4 1.1.7 1.6l-1.4 2 2 2 2-1.4c.5.3 1 .5 1.6.7l.5 2.4h2.8l.5-2.4c.6-.2 1.1-.4 1.6-.7l2 1.4 2-2-1.4-2c.3-.5.5-1 .7-1.6z"/></svg></div>
    <div><h3>Managed IT</h3><p>At vero eos et accusamus et iusto odio dignissimos ducim</p></div>
  </div>
  <div class="service abs" style="left:452px;top:1243px">
    <div class="service-icon"><svg width="30" height="32" viewBox="0 0 24 26"><ellipse cx="12" cy="5" rx="9" ry="3.5" fill="#fff"/><path fill="#fff" d="M3 8c2 3 16 3 18 0v4c-2 3-16 3-18 0zm0 7c2 3 16 3 18 0v4c0 2-4 3.5-9 3.5S3 21 3 19z"/></svg></div>
    <div><h3>Servers</h3><p>At vero eos et accusamus et iusto odio dignissimos ducim</p></div>
  </div>
  <div class="service abs" style="left:813px;top:1243px">
    <div class="service-icon"><svg width="30" height="30" viewBox="0 0 24 24" fill="#fff"><rect x="2" y="3" width="6" height="5"/><rect x="9" y="3" width="6" height="5"/><rect x="16" y="3" width="6" height="5"/><rect x="2" y="9.5" width="6" height="5"/><rect x="9" y="9.5" width="6" height="5"/><rect x="16" y="9.5" width="6" height="5"/><rect x="2" y="16" width="6" height="5"/><rect x="9" y="16" width="6" height="5"/><rect x="16" y="16" width="6" height="5"/></svg></div>
    <div><h3>APPS</h3><p>At vero eos et accusamus et iusto odio dignissimos ducim</p></div>
  </div>
  <div class="service abs" style="left:97px;top:1379px">
    <div class="service-icon"><svg width="36" height="26" viewBox="0 0 28 18"><path fill="#fff" d="M7 18a6 6 0 01-.6-12A8 8 0 0121.5 6.5 5.8 5.8 0 0122 18z"/></svg></div>
    <div><h3>Private Cloud</h3><p>At vero eos et accusamus et iusto odio dignissimos ducim</p></div>
  </div>
  <div class="service abs" style="left:452px;top:1379px">
    <div class="service-icon"><svg width="30" height="30" viewBox="0 0 24 24"><circle cx="12" cy="12" r="10" fill="#fff"/><path fill="#0292cd" d="M8 6l3 2-1 3-3-1zm6 5l3 1v4l-3 2-1-4z"/></svg></div>
    <div><h3>Web</h3><p>At vero eos et accusamus et iusto odio dignissimos ducim</p></div>
  </div>
  <div class="service abs" style="left:813px;top:1379px">
    <div class="service-icon"><svg width="30" height="30" viewBox="0 0 24 24" fill="#fff"><circle cx="18" cy="5" r="3.5"/><circle cx="6" cy="12" r="3.5"/><circle cx="18" cy="19" r="3.5"/><path d="M6 12L18 5M6 12l12 7" stroke="#fff" stroke-width="2"/></svg></div>
    <div><h3>Internet Solutions</h3><p>At vero eos et accusamus et iusto odio dignissimos ducim</p></div>
  </div>

  <h2 class="section-title abs" style="top:1615px;color:var(--ink)">LATEST BLOG</h2>

  <article class="post abs" style="left:97px;top:1689px">
    <div class="post-img"><div role="img" aria-label="Colleagues meeting around an office table" style="background:linear-gradient(135deg,#e6ecf2,#b9c4cf 60%,#4b5866)"></div></div>
    <h3>Finibus Bonorum Llanditet Ma</h3>
    <div class="meta"><svg width="12" height="12" viewBox="0 0 24 24"><path fill="#0292cd" d="M3 5h18v16H3zm2 5v9h14v-9zM7 2h2v4H7zm8 0h2v4h-2z"/></svg>02/08/2017<span class="sep">|</span><svg width="12" height="12" viewBox="0 0 24 24"><circle cx="12" cy="7" r="5" fill="#0292cd"/><path fill="#0292cd" d="M3 22c0-6 4-9 9-9s9 3 9 9z"/></svg>John Doe</div>
    <p>Nam libero tempore, cum soluta nobis est eligendi optio cumque nihil impedit quo minus id quod ma ixime placeat facere possimus</p>
    <div class="btn-line">READ MORE</div>
  </article>
  <article class="post abs" style="left:442px;top:1689px">
    <div class="post-img"><div role="img" aria-label="Open hands holding a glowing network globe" style="background:linear-gradient(135deg,#9fb5cc,#5f7f9f 55%,#2f4560)"></div></div>
    <h3>Finibus Bonorum Llanditet Ma</h3>
    <div class="meta"><svg width="12" height="12" viewBox="0 0 24 24"><path fill="#0292cd" d="M3 5h18v16H3zm2 5v9h14v-9zM7 2h2v4H7zm8 0h2v4h-2z"/></svg>02/08/2017<span class="sep">|</span><svg width="12" height="12" viewBox="0 0 24 24"><circle cx="12" cy="7" r="5" fill="#0292cd"/><path fill="#0292cd" d="M3 22c0-6 4-9 9-9s9 3 9 9z"/></svg>John Doe</div>
    <p>Nam libero tempore, cum soluta nobis est eligendi optio cumque nihil impedit quo minus id quod ma ixime placeat facere possimus</p>
    <div class="btn-line">READ MORE</div>
  </article>
  <article class="post abs" style="left:787px;top:1689px">
    <div class="post-img"><div role="img" aria-label="Glowing blue digital globe on black" style="background:radial-gradient(circle at 60% 50%,#1d6fa8,#0a2540 55%,#000 85%)"></div></div>
    <h3>Finibus Bonorum Llanditet Ma</h3>
    <div class="meta"><svg width="12" height="12" viewBox="0 0 24 24"><path fill="#0292cd" d="M3 5h18v16H3zm2 5v9h14v-9zM7 2h2v4H7zm8 0h2v4h-2z"/></svg>02/08/2017<span class="sep">|</span><svg width="12" height="12" viewBox="0 0 24 24"><circle cx="12" cy="7" r="5" fill="#0292cd"/><path fill="#0292cd" d="M3 22c0-6 4-9 9-9s9 3 9 9z"/></svg>John Doe</div>
    <p>Nam libero tempore, cum soluta nobis est eligendi optio cumque nihil impedit quo minus id quod ma ixime placeat facere possimus</p>
    <div class="btn-line">READ MORE</div>
  </article>

  <section class="reviews abs" role="img" aria-label="Darkened photo of hands working at a desk"></section>
  <h2 class="section-title abs" style="top:2276px;color:var(--white)">CLIENT REVIEWS</h2>
  <div class="arrow abs" style="left:30px;top:2407px"><svg width="10" height="14" viewBox="0 0 10 14"><path d="M8 1L2 7l6 6" fill="none" stroke="#fff" stroke-width="2"/></svg></div>
  <div class="arrow abs" style="left:1134px;top:2407px"><svg width="10" height="14" viewBox="0 0 10 14"><path d="M2 1l6 6-6 6" fill="none" stroke="#fff" stroke-width="2"/></svg></div>

  <div class="review abs" style="left:95px;top:2349px">
    <div class="avatar" role="img" aria-label="Client portrait"></div>
    <div><p class="quote"><b>“</b>At vero eos et accusamus et iustodio dignissimos ducimus qui blanditiipraesnt ium voluptatum deleniti atque cruqquos dolores et quas molestias.</p><p class="who">Marla Fenwick</p><p class="role">Financial Services Professional</p></div>
  </div>
  <div class="review abs" style="left:440px;top:2349px">
    <div class="avatar" role="img" aria-label="Client portrait"></div>
    <div><p class="quote"><b>“</b>At vero eos et accusamus et iustodio dignissimos ducimus qui blanditiipraesnt ium voluptatum deleniti atque cruqquos dolores et quas molestias.</p><p class="who">Tobin R. Ashcroft</p><p class="role">National Urban Fellow at the Houston</p></div>
  </div>
  <div class="review abs" style="left:789px;top:2349px">
    <div class="avatar" role="img" aria-label="Client portrait"></div>
    <div><p class="quote"><b>“</b>At vero eos et accusamus et iustodio dignissimos ducimus qui blanditiipraesnt ium voluptatum deleniti atque cruqquos dolores et quas molestias.</p><p class="who">Petra Lindqvist</p><p class="role">Creative Strategist | Entrepreneur &amp; Upcoming</p></div>
  </div>

  <footer class="footer">
    <div class="brand abs" style="top:2715px"><span class="brand-dot"></span><span class="brand-name">HLE Technologies</span></div>

    <div class="abs" style="left:407px;top:2642px">
      <h4>QUICK LINKS</h4>
      <ul class="links"><li>Home</li><li>Servers</li><li>Networks</li><li>Managed IT</li><li>Web</li><li>App's</li><li>Internet</li><li>Contact</li></ul>
    </div>

    <div class="abs" style="left:592px;top:2642px;width:270px">
      <h4>NEWSLETTER SUBSCRIPTION</h4>
      <p style="margin-top:22px">Register your Email Address to get information about us</p>
      <div class="field" style="margin-top:14px">Email Address</div>
      <div class="btn-line" style="width:104px;height:34px;font-size:11px;margin-top:18px">SUBSCRIBE</div>
    </div>

    <div class="abs" style="left:914px;top:2642px;width:200px">
      <h4>CONTACT US</h4>
      <div class="contact-row" style="margin-top:22px"><svg width="12" height="16" viewBox="0 0 12 16" style="margin-top:3px"><path fill="#0255a3" d="M6 0a6 6 0 00-6 6c0 4.5 6 10 6 10s6-5.5 6-10a6 6 0 00-6-6zm0 8.5A2.5 2.5 0 116 3.5a2.5 2.5 0 010 5z"/></svg><span>4b 2210 Harbour Rd, Upper<br>Kelvin Grove</span></div>
      <div class="contact-row" style="margin-top:24px"><svg width="14" height="14" viewBox="0 0 24 24" style="margin-top:3px"><path fill="#0255a3" d="M6.6 10.8a15 15 0 006.6 6.6l2.2-2.2c.3-.3.7-.4 1-.2 1.1.4 2.3.6 3.6.6.6 0 1 .4 1 1V20c0 .6-.4 1-1 1A17 17 0 013 4c0-.6.4-1 1-1h3.5c.6 0 1 .4 1 1 0 1.3.2 2.5.6 3.6.1.3 0 .7-.2 1z"/></svg><span>1300 555 014</span></div>
      <div class="contact-row" style="margin-top:20px"><svg width="14" height="14" viewBox="0 0 24 24" style="margin-top:3px"><path fill="#0255a3" d="M2 5h20v14H2zm2 2v.5l8 5 8-5V7l-8 5z"/></svg><span>info@hle.com.au</span></div>
    </div>

    <div class="rule abs"></div>
    <p class="copy abs">Copyrights © 2017, HLE Technologies.&nbsp; All rights reserved.</p>
    <div class="social abs"><i></i><i></i><i></i><i></i></div>
  </footer>

</div>
</body>
</html>
```